Amber Ridge Partners Business Card

A business card design to accompany the logo design you completed on Pixel Forum. We are open to your proposals. I did add one idea below that might work, but we aren't married to the idea. The company is a real estate services company. Clientele are typically high net worth individuals, executive level employment or owners of their own company, 30-60 years old.

Our 1 (bad?) idea: double sided card; One side landscape with logo and word mark. Other side Portrait with the logo only (oversize watermark maybe?). Somewhere add text of Name (Marcus Tellingham), Title (Principal), phone # (555-214-7736) and email address (marcus@amberridgeco.example). There would be a second design with my wife's name, number and email in place of mine.

Again totally open to ideas here.

Industry/Entity Type

Real Estate

```html
<!DOCTYPE html>
<html lang="en">
<head>
<meta charset="utf-8">
<title>Amber Ridge Partners Business Card</title>
<link rel="stylesheet" href="https://fonts.googleapis.com/css2?family=Cabin:wght@400&display=swap">
<style>
  :root {
    --page-bg: #f2f2f0;
    --card-bg: #ffffff;
    --brand-green: #4f8d48;
    --brand-green-light: #7fb374;
    --ink-grey: #4a4a4a;
    --card-shadow: rgba(0, 0, 0, 0.28);
  }
  * { margin: 0; padding: 0; box-sizing: border-box; }
  html, body {
    width: 1200px;
    height: 1198px;
    overflow: hidden;
    background: var(--page-bg);
    font-family: "Cabin", "Gill Sans", sans-serif;
  }
  .card-sheet {
    position: relative;
    width: 1200px;
    height: 1198px;
  }
  .card {
    position: absolute;
    left: 160px;
    width: 880px;
    height: 503px;
    background: var(--card-bg);
    box-shadow: 0 6px 14px var(--card-shadow);
  }
  .card--front { top: 56px; }
  .card--back  { top: 631px; }

  .holder {
    position: absolute;
    right: 42px;
    top: 44px;
    text-align: right;
  }
  .holder__name {
    font-size: 40px;
    color: var(--ink-grey);
    line-height: 1.1;
  }
  .holder__title {
    font-size: 34px;
    color: var(--brand-green);
    line-height: 1.3;
  }

  .brand {
    position: absolute;
    left: 48px;
    top: 186px;
    display: flex;
    align-items: center;
    gap: 34px;
  }
  .brand__dot {
    width: 108px;
    height: 108px;
    border-radius: 50%;
    background: var(--brand-green);
  }
  .brand__name {
    font-size: 46px;
    color: var(--brand-green);
    letter-spacing: 1px;
  }

  .contact {
    position: absolute;
    right: 42px;
    bottom: 40px;
    text-align: right;
    font-size: 31px;
    color: var(--ink-grey);
    line-height: 1.5;
  }
  .contact__email-at { color: var(--brand-green); }

  .back-pattern {
    position: absolute;
    inset: 0;
    background: linear-gradient(135deg, var(--brand-green) 0%, var(--brand-green-light) 50%, var(--brand-green) 100%);
  }
</style>
</head>
<body>
  <main class="card-sheet">
    <section class="card card--front">
      <div class="holder">
        <p class="holder__name">Marcus Tellingham</p>
        <p class="holder__title">Principal</p>
      </div>
      <div class="brand">
        <span class="brand__dot"></span>
        <span class="brand__name">Amber Ridge Partners</span>
      </div>
      <div class="contact">
        <p class="contact__phone">555-214-7736</p>
        <p class="contact__email">marcus<span class="contact__email-at">@amberridgeco</span>.example</p>
      </div>
    </section>

    <section class="card card--back">
      <div class="back-pattern" role="img" aria-label="Repeating green and white brand emblem pattern covering the back of the card"></div>
    </section>
  </main>
</body>
</html>
```